Financial Advisory Firm needs a custom content template for financial topics

I need a template that I can reuse often to deliver financial advice commentary on topics ranging from investments to financial planning ideas to tax planning strategies. I am hoping to get a template that is visually exciting and captures readers attention. I will use this template to regularly create new financial and tax content that I will post to social media (e.g. Brivora), my website and targeted email campaigns to current and prospective clients. The content will never be greater than 2 pages.

```html
<!DOCTYPE html>
<html lang="en">
<head>
<meta charset="utf-8">
<title>Summit Ledger – Letterhead Template</title>
<link href="https://fonts.googleapis.com/css2?family=Tinos:wght@400;700&family=PT+Sans:ital@0;1&family=Arimo&display=swap" rel="stylesheet">
<style>
  :root {
    --gold: #f2b631;
    --gold-deep: #e0a20f;
    --gold-light: #fbe7b4;
    --blue-light: #4cb0e6;
    --blue-deep: #0f4f80;
    --navy: #0c1827;
    --ink-blue: #1f7fc4;
    --white: #ffffff;
  }
  * { margin: 0; padding: 0; box-sizing: border-box; }
  html, body { width: 848px; height: 1200px; overflow: hidden; background: var(--white); }
  .page { position: relative; width: 848px; height: 1200px; background: var(--white); }

  .masthead { position: absolute; top: 0; left: 0; width: 848px; height: 202px; }
  .masthead svg { position: absolute; inset: 0; display: block; }

  .brand-name {
    position: absolute; left: 108px; top: 74px;
    display: flex; align-items: center; gap: 12px;
    font-family: "Tinos", serif; font-weight: 700; font-size: 38px;
    color: var(--ink-blue); letter-spacing: 0.5px;
  }
  .brand-mark { width: 18px; height: 18px; border-radius: 50%; background: var(--ink-blue); }

  .contact-block {
    position: absolute; right: 102px; top: 56px; text-align: right;
    font-family: "Tinos", serif; color: var(--white); line-height: 1.15;
  }
  .contact-block .firm { font-weight: 700; font-size: 21px; color: var(--gold); margin-bottom: 2px; }
  .contact-block .advisor, .contact-block .role { font-size: 14.5px; }
  .contact-block .phones { margin-top: 6px; font-size: 14.5px; }

  .info-bar {
    position: absolute; top: 202px; left: 0; width: 848px; height: 21px;
    background: var(--navy); color: var(--white);
    font-family: "PT Sans", sans-serif; font-size: 14px;
    display: flex; justify-content: space-between; align-items: center;
    padding: 0 102px 0 101px;
  }
  .info-bar em { font-style: italic; }

  .body-area { position: absolute; top: 223px; left: 0; width: 848px; height: 867px; }

  .disclaimer {
    position: absolute; bottom: 0; left: 0; width: 848px; height: 110px;
    background: var(--navy); color: var(--white);
    font-family: "Arimo", sans-serif; font-size: 11.3px; line-height: 17.6px;
    text-align: center; padding: 24px 100px 0;
  }
</style>
</head>
<body>
<div class="page">
  <header class="masthead">
    <svg width="848" height="202" viewBox="0 0 848 202" aria-hidden="true">
      <defs>
        <linearGradient id="goldFill" x1="0" y1="0" x2="0" y2="1">
          <stop offset="0" stop-color="var(--gold-deep)"/>
          <stop offset="0.6" stop-color="var(--gold)"/>
          <stop offset="1" stop-color="var(--gold-light)"/>
        </linearGradient>
        <linearGradient id="blueFill" x1="0" y1="0" x2="0" y2="1">
          <stop offset="0" stop-color="var(--blue-light)"/>
          <stop offset="0.55" stop-color="#1e6fa6"/>
          <stop offset="1" stop-color="var(--blue-deep)"/>
        </linearGradient>
      </defs>
      <rect class="sky-band" width="848" height="202" fill="url(#blueFill)"/>
      <path class="gold-wave" d="M0 0 H720 C600 8 480 50 380 120 C320 165 250 195 160 202 H0 Z" fill="url(#goldFill)"/>
      <path class="wave-glow" d="M720 0 C600 8 480 50 380 120 C320 165 250 195 160 202" fill="none" stroke="#fff6dc" stroke-width="3" opacity="0.7"/>
    </svg>
    <div class="brand-name"><span class="brand-mark"></span>Summit Ledger</div>
    <div class="contact-block">
      <div class="firm">Summit Ledger</div>
      <div class="advisor">Daniel Ashworth CFP<sup>®</sup>, CPA</div>
      <div class="role">Personal CFO</div>
      <div class="phones">t: 555-201-4830<br>t: 555-201-4871</div>
    </div>
  </header>

  <div class="info-bar">
    <span>visit us: <em>www.summitledger.com</em></span>
    <span>mail us: info<em>@summitledger.com</em></span>
  </div>

  <main class="body-area"></main>

  <footer class="disclaimer">
    Summit Ledger, LLC is a registered investment adviser in the state of Washington.&nbsp; The Adviser may not transact business
    in states where it is not appropriately registered or exempt from registration.&nbsp; Individualized responses to persons that involve
    either the effecting of transactions in securities or the rendering of personalized investment advice for compensation will not be
    made without registration or exemption.
  </footer>
</div>
</body>
</html>
```